Post Card Invitation to Wedding Rehearsal Dinner and After Party

This post card should serve as invitations for two events in the wedding weekend for two San Francisco grooms, Derek and Simon.
Each side of the card should have distinct looks and information but tied together with “Before” on the front and “After” on the back.
POST CARD FRONT
Required text:
BEFORE
Derek and Simon’s Wedding: Rehearsal Dinner
Friday, May 22, 2015
5:30 PM
Larkvale Grub Yard
617 Tessler Avenue @ Marlow
San Francisco, CA
Please also convey the following information without necessarily quoting directly: This rehearsal dinner will be held in a private enclosed space in the food truck park. We we will serve beer and wine in our space and provide tickets to purchase food from any of the trucks in the park. Dress is casual.
Look and feel of the card should have a modern, “hipster” feel to it. If you search Google images for “Hipster design” or “hipster infographic” you should get a sense of the overall design and colors. The website for the venue is http://larkvalegrubyard.com/ for reference but please DO NOT use any images or logos from the site.
----------------------
POST CARD REVERSE
Required Text:
AFTER
Derek and Simon’s Wedding: After Party
Saturday, May 23, 2015
7:30 PM
Corvell Harbor Sailing Club
42 Pennick Lane
San Francisco, CA
Please also convey the following information without necessarily quoting directly: Black-tie optional. Dancing, snacks and dessert and cocktails with panoramic views of the San Francisco Bay and Golden Gate Bridge.
This should have a much different look and feel from the front of the card. It should convey an elegant black-tie affair. If you search Google images for “black tie after party invitation” you should get some examples of an overall feel that I am aiming for. The website for the venue is www.chsclub.com but DO NOT use any of the images or logos from the site.
Industry/Entity Type
Wedding
Look and feel
Each slider illustrates characteristics of the customer's brand and the style your logo design should communicate.

```html
<!DOCTYPE html>
<html lang="en">
<head>
<meta charset="utf-8">
<title>Derek and Simon’s Wedding – Rehearsal Dinner &amp; After Party</title>
<link rel="stylesheet" href="https://fonts.googleapis.com/css2?family=Kreon:wght@400;600&family=Oswald:wght@500;600&family=Open+Sans:wght@400&family=Tinos&display=swap">
<style>
  :root {
    --backdrop: #d9d6d1;
    --card: #fbfbfa;
    --card-damask: #f0f1f1;
    --slate: #4f6a80;
    --slate-soft: #c3ced7;
    --hat-grey: #5b5b5b;
    --hat-black: #151515;
    --heading-brown: #5e4c2f;
    --date-brown: #3a2a1e;
    --detail-tan: #a47f66;
    --before-grey: #b4b4b4;
    --rule: #8f7a62;
  }
  * { box-sizing: border-box; margin: 0; padding: 0; }
  html, body { width: 1200px; height: 953px; overflow: hidden; }
  body { background: var(--backdrop); position: relative; }

  .postcard {
    position: absolute; top: 89px; width: 502px; height: 775px;
    background: var(--card); overflow: hidden;
    box-shadow: 0 4px 14px rgba(0,0,0,.18);
  }
  .postcard--front { left: 60px; }
  .postcard--back { left: 640px; background: var(--card-damask); }

  .line { position: absolute; left: 0; right: 0; text-align: center; line-height: 1; }

  .argyle-band { position: absolute; left: 0; right: 0; background: var(--slate); opacity: .85; }
  .argyle-band--top { top: 0; height: 133px; border-bottom: 4px solid var(--slate); }
  .argyle-band--bottom { bottom: 0; height: 36px; border-top: 4px solid var(--slate); }

  .hats { position: absolute; border-radius: 50% 50% 40% 40%; }
  .hats--bowler { left: 128px; top: 90px; width: 236px; height: 114px; background: var(--hat-grey); }
  .hats--top { left: 150px; top: 62px; width: 202px; height: 102px; background: var(--hat-black); border-radius: 8px; z-index: 2; }

  .scroll-band { position: absolute; left: 0; right: 0; background: var(--slate); }
  .scroll-band--top { top: 0; height: 104px; }
  .scroll-band--bottom { bottom: 0; height: 74px; }

  .event-tag { font-family: "Tinos", serif; font-size: 24px; color: var(--before-grey); letter-spacing: .5px; }
  .event-tag--after { color: #111; font-size: 23px; }
  .couple { font-family: "Kreon", serif; font-weight: 600; font-size: 24px; color: var(--heading-brown); }
  .event-name { font-family: "Kreon", serif; font-weight: 600; font-size: 40px; color: var(--heading-brown); }
  .venue { font-family: "Kreon", serif; font-weight: 600; font-size: 27px; color: var(--heading-brown); }
  .address, .dress { font-family: "Tinos", serif; font-size: 18px; color: var(--detail-tan); line-height: 25px; }

  .rule { position: absolute; height: 2px; background: var(--rule); }
  .rule--thin { height: 1px; background: #d5cabd; }

  .date-block {
    position: absolute; height: 62px;
    border-top: 2px solid var(--slate); border-bottom: 2px solid var(--slate);
    font-family: "Oswald", sans-serif; font-weight: 600; font-size: 58px;
    color: var(--date-brown); line-height: 56px; text-align: center;
  }
  .date-ring { position: absolute; width: 160px; height: 160px; }
  .date-ring text { font-family: "Open Sans", sans-serif; fill: var(--date-brown); }
  .date-ring .day-num { font-family: "Oswald", sans-serif; font-weight: 500; font-size: 50px; }

  .flourish { position: absolute; height: 42px; background: var(--slate-soft); border-radius: 21px; }
</style>
</head>
<body>

<section class="postcard postcard--front" aria-label="Rehearsal dinner invitation">
  <div class="argyle-band argyle-band--top" role="img" aria-label="Slate blue and white argyle pattern"></div>
  <div class="hats hats--bowler" role="img" aria-label="Two grey bowler hats"></div>

  <p class="line event-tag" style="top:195px">BEFORE</p>
  <p class="line couple" style="top:232px">Derek and Simon’s Wedding</p>
  <div class="rule" style="left:83px; width:328px; top:264px"></div>
  <h1 class="line event-name" style="top:273px">Rehearsal Dinner</h1>

  <div class="date-block" style="left:90px; width:110px; top:395px">MAY</div>
  <div class="date-block" style="left:312px; width:104px; top:395px">2015</div>
  <svg class="date-ring" style="left:166px; top:347px" viewBox="0 0 160 160" aria-label="Friday, 22, 5:30 PM">
    <defs>
      <path id="front-top-arc" d="M22 80 A58 58 0 0 1 138 80"/>
      <path id="front-bottom-arc" d="M12 80 A68 68 0 0 0 148 80"/>
    </defs>
    <circle cx="80" cy="80" r="51" fill="none" stroke="var(--slate)" stroke-width="3"/>
    <text font-size="18"><textPath href="#front-top-arc" startOffset="50%" text-anchor="middle">FRIDAY</textPath></text>
    <text class="day-num" x="80" y="98" text-anchor="middle">22</text>
    <text font-size="17"><textPath href="#front-bottom-arc" startOffset="50%" text-anchor="middle">5:30 PM</textPath></text>
  </svg>
  <div class="flourish" style="left:80px; width:100px; top:478px" role="img" aria-label="Slate scroll flourish"></div>
  <div class="flourish" style="left:318px; width:104px; top:478px" role="img" aria-label="Slate scroll flourish"></div>

  <h2 class="line venue" style="top:560px">Larkvale Grub Yard</h2>
  <div class="rule rule--thin" style="left:102px; width:306px; top:598px"></div>
  <p class="line address" style="top:607px">617 Tessler Avenue @ Marlow<br>San Francisco, CA</p>
  <p class="line dress" style="top:677px">Casual dress</p>

  <div class="argyle-band argyle-band--bottom" role="img" aria-label="Slate blue and white argyle pattern"></div>
</section>

<section class="postcard postcard--back" aria-label="After party invitation">
  <div class="scroll-band scroll-band--top" role="img" aria-label="Slate band with white scrollwork ornament"></div>
  <div class="hats hats--top" role="img" aria-label="Two black top hats"></div>

  <p class="line event-tag event-tag--after" style="top:180px">AFTER</p>
  <p class="line couple" style="top:217px">Derek and Simon’s Wedding</p>
  <div class="rule" style="left:92px; width:326px; top:247px"></div>
  <h1 class="line event-name" style="top:255px">After Party</h1>

  <div class="date-block" style="left:92px; width:104px; top:368px">MAY</div>
  <div class="date-block" style="left:318px; width:104px; top:368px">2015</div>
  <svg class="date-ring" style="left:172px; top:320px" viewBox="0 0 160 160" aria-label="Saturday, 23, 7:30 PM">
    <defs>
      <path id="back-top-arc" d="M22 80 A58 58 0 0 1 138 80"/>
      <path id="back-bottom-arc" d="M12 80 A68 68 0 0 0 148 80"/>
    </defs>
    <circle cx="80" cy="80" r="51" fill="none" stroke="var(--slate)" stroke-width="3"/>
    <text font-size="18"><textPath href="#back-top-arc" startOffset="50%" text-anchor="middle">SATURDAY</textPath></text>
    <text class="day-num" x="80" y="98" text-anchor="middle">23</text>
    <text font-size="17"><textPath href="#back-bottom-arc" startOffset="50%" text-anchor="middle">7:30 PM</textPath></text>
  </svg>
  <div class="flourish" style="left:82px; width:104px; top:448px" role="img" aria-label="Slate scroll flourish"></div>
  <div class="flourish" style="left:322px; width:104px; top:448px" role="img" aria-label="Slate scroll flourish"></div>

  <h2 class="line venue" style="top:524px">Corvell Harbor Sailing Club</h2>
  <div class="rule rule--thin" style="left:98px; width:314px; top:563px"></div>
  <p class="line address" style="top:572px">42 Pennick Lane<br>San Francisco, CA</p>
  <p class="line dress" style="top:641px">Black-tie optional.</p>

  <div class="scroll-band scroll-band--bottom" role="img" aria-label="Slate band with white scrollwork ornament"></div>
</section>

</body>
</html>
```